Forest Consultant/Timber Buyer needs a clean business card

We are a forestry consulting and timber buying company. We meet with private landowners and assist them with timber management and timber harvesting. We would like a professional business card, please no clip art. logo is blue and white but would like to see a gray,silver, or some other color incorporated. Would like basic contact info. Would like to the layout to be creative and sleek but masculine.

Target Market(s)

private landowners

Industry/Entity Type

Business

Contact Information for Business Card

name,position, cell number, office number, email, website. This might be to cluttered. Basic contact info is what we are looking for.

Contact info can all be on one side with logo on the other.

Font styles to use
Serif
Sans Serif

Colors
0255a3
ffffff
aaaaaa

Requirements
Must have
• We just want it professional.
Nice to have
• Creative layout.
Should not have
• please no clip art of log trucks etc.

```html
<!DOCTYPE html>
<html lang="en">
<head>
<meta charset="utf-8">
<title>Heartwood Land &amp; Timber – Business Card</title>
<link rel="stylesheet" href="https://fonts.googleapis.com/css2?family=Lato:wght@400;700&display=swap">
<style>
  :root {
    --stage: #262626;
    --card-dark: #141414;
    --card-mid: #2b2b2b;
    --card-light: #3d3d3d;
    --ink-white: #ffffff;
    --ink-silver: #aaaaaa;
    --ink-soft: #d4d4d4;
  }
  * { margin: 0; padding: 0; box-sizing: border-box; }
  html, body {
    width: 1200px;
    height: 997px;
    overflow: hidden;
    background: var(--stage);
    font-family: "Lato", sans-serif;
  }
  .stage {
    position: relative;
    width: 1200px;
    height: 997px;
  }
  .card {
    position: absolute;
    left: 250px;
    width: 700px;
    height: 400px;
    border-radius: 22px;
    overflow: hidden;
    box-shadow: 0 18px 40px rgba(0,0,0,0.55);
  }
  .card--front { top: 80px; }
  .card--back  { top: 517px; }
  .card__facets {
    position: absolute;
    inset: 0;
    background:
      radial-gradient(ellipse at 30% 25%, var(--card-light) 0%, transparent 55%),
      radial-gradient(ellipse at 80% 75%, var(--card-mid) 0%, transparent 60%),
      linear-gradient(135deg, var(--card-mid) 0%, var(--card-dark) 55%, var(--card-mid) 100%);
  }
  .brand {
    position: absolute;
    display: flex;
    align-items: center;
    gap: 18px;
    color: var(--ink-white);
  }
  .brand__dot {
    width: 74px;
    height: 74px;
    border-radius: 50%;
    background: var(--ink-white);
    flex: none;
  }
  .brand__name {
    font-weight: 700;
    font-size: 44px;
    letter-spacing: 3px;
    line-height: 1;
  }
  .brand__tagline {
    margin-top: 8px;
    font-weight: 700;
    font-size: 14px;
    letter-spacing: 6px;
    text-align: right;
  }
  .card--front .brand {
    left: 50%;
    top: 50%;
    transform: translate(-50%, -50%);
  }
  .card--back .brand {
    left: 48px;
    top: 160px;
  }
  .card--back .brand__dot { width: 62px; height: 62px; }
  .card--back .brand__name { font-size: 36px; }
  .card--back .brand__tagline { font-size: 12px; letter-spacing: 5px; }
  .divider {
    position: absolute;
    left: 418px;
    top: 118px;
    width: 1px;
    height: 170px;
    background: linear-gradient(to bottom, transparent, var(--ink-silver), transparent);
  }
  .contact {
    position: absolute;
    left: 446px;
    top: 104px;
    color: var(--ink-soft);
  }
  .contact__name {
    font-size: 20px;
    font-weight: 700;
    letter-spacing: 1px;
    color: var(--ink-white);
    text-transform: uppercase;
  }
  .contact__role {
    font-size: 13px;
    color: var(--ink-silver);
    margin-top: 2px;
  }
  .contact__list {
    list-style: none;
    margin-top: 34px;
  }
  .contact__item {
    display: flex;
    align-items: center;
    gap: 12px;
    font-size: 12.5px;
    letter-spacing: 0.4px;
    margin-bottom: 12px;
  }
  .contact__icon {
    width: 13px;
    height: 13px;
    flex: none;
    fill: none;
    stroke: var(--ink-silver);
    stroke-width: 1.4;
  }
</style>
</head>
<body>
<main class="stage">

  <section class="card card--front" aria-label="Business card front">
    <div class="card__facets" role="img" aria-label="Faceted low-poly pattern in charcoal and dark gray tones"></div>
    <div class="brand">
      <span class="brand__dot"></span>
      <div>
        <div class="brand__name">HEARTWOOD</div>
        <div class="brand__tagline">LAND &amp; TIMBER</div>
      </div>
    </div>
  </section>

  <section class="card card--back" aria-label="Business card back">
    <div class="card__facets" role="img" aria-label="Faceted low-poly pattern in charcoal and dark gray tones"></div>
    <div class="brand">
      <span class="brand__dot"></span>
      <div>
        <div class="brand__name">HEARTWOOD</div>
        <div class="brand__tagline">LAND &amp; TIMBER</div>
      </div>
    </div>
    <div class="divider"></div>
    <div class="contact">
      <div class="contact__name">Daniel Mercer</div>
      <div class="contact__role">Chief Executive Officer</div>
      <ul class="contact__list">
        <li class="contact__item">
          <svg class="contact__icon" viewBox="0 0 13 13"><rect x="1.5" y="1.5" width="10" height="10"/></svg>
          <span>+852 5550 0142</span>
        </li>
        <li class="contact__item">
          <svg class="contact__icon" viewBox="0 0 13 13"><rect x="1" y="3" width="11" height="7.5"/><path d="M1 3 L6.5 7.5 L12 3"/></svg>
          <span>hello@heartwoodtimber.com</span>
        </li>
        <li class="contact__item">
          <svg class="contact__icon" viewBox="0 0 13 13"><path d="M6.5 12 C3 8 2.5 6.5 2.5 5 A4 4 0 0 1 10.5 5 C10.5 6.5 10 8 6.5 12 Z"/><circle cx="6.5" cy="5" r="1.3"/></svg>
          <span>Cedar Court F12-14, Pine Harbour</span>
        </li>
      </ul>
    </div>
  </section>

</main>
</body>
</html>
```